We need a professional looking 4 x 9 Rack Card

I need a 2 sided 4 x 9 rack card for my boat charter business. Please see website (www.tidewispcruise.com) and attached files for the type of look and artwork we've used thus far. And see some attached examples that competitors are using. Please don't copy these ideas...I just sent them so you can understand what others are doing and what I think looks good and what looks bad. I'm looking for you to provide your best ideas.

Target Market(s)

Hotel and resort tourists who visit Clearwater Beach and surrounding areas.

Industry/Entity Type

Business

Colors

Designer to choose colors to be used in the design.

Requirements
Must have
• The top 1/4 of the front side is most important to have strong headline/artwork. Need powerful imagery. I will pay for images you need. Please review website to gain understanding of what we are selling. www.tidewispcruise.com. I'd like designers to offer their best messaging ideas based on their impression of what will be appealing to target market. To help, please know that our customers want to go boating but instead of renting a boat themselves, they hire us to take them out. Some of the favorite things we do are to go dolphin watching, sunset cruises, and taking them to private, secluded beaches where they can walk and look for seashells. I want it to be a simple design, not cluttered.
Nice to have
• website (www.tidewispcruise.com), phone (555)-203-7714, email address (info@tidewispcruise.com), tripadvisor logo, facebook logo, youtube logo, instagram logo,
Should not have
• Do not need mailing address on the card.

```html
<!DOCTYPE html>
<html lang="en">
<head>
<meta charset="utf-8">
<title>Tidewisp Cruise Rack Card</title>
<link rel="stylesheet" href="https://fonts.googleapis.com/css2?family=Oswald:wght@400;500;600&family=Dosis:wght@500;600;700&family=Poppins:wght@400;500&display=swap">
<style>
  :root {
    --orange-light: #f9a12a;
    --orange: #f58220;
    --orange-deep: #ef6b1f;
    --blue: #1fa3e0;
    --blue-deep: #1482c4;
    --navy: #1d3f8e;
    --ink: #1c1c1c;
    --white: #ffffff;
    --sky-top: #ffffff;
    --sky-bottom: #dbeefa;
    --page: #e6e6e6;
  }
  * { box-sizing: border-box; margin: 0; padding: 0; }
  html, body { width: 792px; height: 1200px; overflow: hidden; }
  body {
    background: var(--page);
    font-family: "Dosis", sans-serif;
    position: relative;
  }
  .card {
    position: absolute;
    top: 218px;
    width: 340px;
    height: 765px;
    overflow: hidden;
    background: linear-gradient(180deg, var(--sky-top) 0%, var(--sky-bottom) 45%);
    box-shadow: 0 6px 18px rgba(0,0,0,0.25);
  }
  .card--front { left: 36px; }
  .card--back { left: 416px; }

  .brand {
    position: absolute;
    top: 22px; left: 0; right: 0;
    text-align: center;
  }
  .brand__name {
    display: inline-flex;
    align-items: center;
    gap: 8px;
    font-family: "Poppins", sans-serif;
    font-weight: 400;
    font-size: 20px;
    color: var(--ink);
    line-height: 1;
  }
  .brand__dot {
    width: 14px; height: 14px;
    border-radius: 50%;
    background: var(--ink);
  }
  .brand__tag {
    margin-top: 7px;
    font-family: "Poppins", sans-serif;
    font-size: 8.5px;
    color: var(--navy);
    letter-spacing: 0.2px;
  }

  .headline {
    position: absolute;
    top: 92px; left: 0; right: 0;
    text-align: center;
    font-family: "Oswald", sans-serif;
    font-weight: 500;
    font-size: 42px;
    color: var(--orange-deep);
    line-height: 1;
    letter-spacing: -0.5px;
    white-space: nowrap;
  }
  .subline {
    position: absolute;
    top: 140px; left: 0; right: 0;
    text-align: center;
    font-family: "Poppins", sans-serif;
    font-size: 7.5px;
    color: var(--ink);
    white-space: nowrap;
  }

  .photo {
    position: absolute;
    left: 0; right: 0;
  }
  .card--front .photo {
    top: 155px; height: 225px;
    background: linear-gradient(180deg, #9cc9e8 0%, #d7e6f0 45%, #b9c4cc 75%, #6f7880 100%);
  }
  .card--back .photo {
    top: 92px; height: 290px;
    background: linear-gradient(180deg, #ffffff 0%, #c3d9e8 30%, #3a3e44 52%, #5fb5a6 60%, #8fd3c4 100%);
  }

  .wave {
    position: absolute;
    left: 0; top: 330px;
    width: 340px; height: 90px;
    display: block;
  }
  .panel {
    position: absolute;
    left: 0; right: 0;
    top: 418px; bottom: 0;
    background: linear-gradient(180deg, var(--orange) 0%, var(--orange-light) 55%, var(--orange) 100%);
  }

  .footer-shape {
    position: absolute;
    left: 0; bottom: 0;
    width: 340px; height: 80px;
    display: block;
  }

  /* Front panel */
  .offer-title {
    position: absolute;
    top: 448px; left: 30px;
    font-family: "Oswald", sans-serif;
    font-weight: 400;
    font-size: 29px;
    line-height: 38px;
    letter-spacing: -0.2px;
    white-space: nowrap;
    color: var(--white);
  }
  .feature-list {
    position: absolute;
    top: 546px; left: 30px;
    list-style: none;
  }
  .feature-list li {
    display: flex;
    align-items: center;
    gap: 12px;
    font-family: "Dosis", sans-serif;
    font-weight: 500;
    font-size: 15px;
    color: var(--white);
    line-height: 21.5px;
    white-space: nowrap;
  }
  .feature-list svg { width: 20px; height: 10px; flex: none; }

  /* Footer */
  .contact {
    position: absolute;
    bottom: 11px; right: 16px;
    padding-left: 8px;
    border-left: 1px solid rgba(255,255,255,0.8);
    font-family: "Poppins", sans-serif;
    font-size: 11.5px;
    line-height: 18px;
    color: var(--white);
    white-space: nowrap;
  }
  .contact__row { display: flex; align-items: center; gap: 5px; }
  .contact__row svg { width: 11px; height: 11px; flex: none; }
  .social {
    position: absolute;
    bottom: 12px; left: 28px;
    display: flex; gap: 8px;
  }
  .social__dot {
    width: 20px; height: 20px; border-radius: 50%;
  }
  .social__dot--a { background: var(--navy); }
  .social__dot--b { background: #d63a2c; }
  .social__dot--c { background: #3b5f86; }
  .listing-badge {
    position: absolute;
    bottom: 15px; left: 34px;
    width: 82px; height: 24px;
    border-radius: 4px;
    background: var(--white);
    opacity: 0.9;
  }

  /* Back panel */
  .boat-spec {
    position: absolute;
    top: 462px; left: 0; right: 0;
    text-align: center;
    color: var(--navy);
    white-space: nowrap;
  }
  .boat-spec__line1 {
    font-family: "Dosis", sans-serif;
    font-weight: 700;
    font-size: 15px;
    letter-spacing: 0.6px;
    word-spacing: 3px;
  }
  .boat-spec__line2 {
    font-family: "Oswald", sans-serif;
    font-weight: 500;
    font-size: 26px;
    line-height: 1.1;
  }
  .divider {
    position: absolute;
    top: 525px; left: 30px; right: 30px;
    height: 1px; background: rgba(255,255,255,0.7);
  }
  .promise {
    position: absolute;
    top: 537px; left: 0; right: 0;
    text-align: center;
    font-family: "Dosis", sans-serif;
    font-weight: 700;
    font-size: 21px;
    line-height: 27px;
    color: var(--white);
  }
  .cta {
    position: absolute;
    top: 603px; left: 41px; right: 41px;
    height: 38px;
    border-radius: 19px;
    background: var(--white);
    box-shadow: 0 2px 4px rgba(0,0,0,0.2);
    display: flex; align-items: center; justify-content: center;
    font-family: "Oswald", sans-serif;
    font-weight: 500;
    font-size: 16px;
    color: var(--orange-deep);
    white-space: nowrap;
  }
  .phone {
    position: absolute;
    top: 652px; left: 0; right: 0;
    display: flex; align-items: center; justify-content: center; gap: 8px;
    font-family: "Oswald", sans-serif;
    font-weight: 400;
    font-size: 24px;
    color: var(--white);
  }
  .phone svg { width: 22px; height: 22px; }
</style>
</head>
<body>

<!-- Front side -->
<section class="card card--front">
  <div class="brand">
    <div class="brand__name"><span class="brand__dot"></span>tidewisp cruise</div>
    <div class="brand__tag">DOLPHIN TOURS AND BOAT CRUISES</div>
  </div>
  <h1 class="headline">LET'S GO BOATING!</h1>
  <p class="subline">Dolphin tours, sunset cruises, private beach walks and sightseeing!</p>

  <div class="photo" role="img" aria-label="Photo of a cheerful group raising their arms aboard a boat under a blue sky"></div>

  <div class="panel"></div>
  <svg class="wave" viewBox="0 0 340 90" preserveAspectRatio="none" aria-hidden="true">
    <path d="M0,38 C90,10 200,62 340,24 L340,42 C200,80 90,28 0,56 Z" fill="#ffffff"/>
    <path d="M0,52 C90,26 200,78 340,40 L340,62 C200,98 90,46 0,76 Z" fill="#1fa3e0"/>
    <path d="M0,74 C90,44 200,96 340,60 L340,90 L0,90 Z" fill="#f58220"/>
  </svg>

  <h2 class="offer-title">PRIVATE BOAT CHARTERS<br>FOR SMALL GROUPS</h2>
  <ul class="feature-list">
    <li><svg viewBox="0 0 20 10"><path d="M1,5 H15 M11,1 L16,5 L11,9" stroke="#fff" stroke-width="2" fill="none" stroke-linecap="round" stroke-linejoin="round"/></svg>Dolphin Tours</li>
    <li><svg viewBox="0 0 20 10"><path d="M1,5 H15 M11,1 L16,5 L11,9" stroke="#fff" stroke-width="2" fill="none" stroke-linecap="round" stroke-linejoin="round"/></svg>Beautiful Sunset Cruises</li>
    <li><svg viewBox="0 0 20 10"><path d="M1,5 H15 M11,1 L16,5 L11,9" stroke="#fff" stroke-width="2" fill="none" stroke-linecap="round" stroke-linejoin="round"/></svg>Secluded Beach Tours</li>
    <li><svg viewBox="0 0 20 10"><path d="M1,5 H15 M11,1 L16,5 L11,9" stroke="#fff" stroke-width="2" fill="none" stroke-linecap="round" stroke-linejoin="round"/></svg>Great Family Fun</li>
    <li><svg viewBox="0 0 20 10"><path d="M1,5 H15 M11,1 L16,5 L11,9" stroke="#fff" stroke-width="2" fill="none" stroke-linecap="round" stroke-linejoin="round"/></svg>Swimming and Snorkeling</li>
    <li><svg viewBox="0 0 20 10"><path d="M1,5 H15 M11,1 L16,5 L11,9" stroke="#fff" stroke-width="2" fill="none" stroke-linecap="round" stroke-linejoin="round"/></svg>Small Groups &amp; Parties</li>
  </ul>

  <svg class="footer-shape" viewBox="0 0 340 80" preserveAspectRatio="none" aria-hidden="true">
    <path d="M0,30 C110,8 230,6 340,22 L340,80 L0,80 Z" fill="#ffffff"/>
    <path d="M0,40 C110,18 230,16 340,32 L340,80 L0,80 Z" fill="#1fa3e0"/>
  </svg>
  <div class="social" aria-label="Social channels">
    <span class="social__dot social__dot--a"></span>
    <span class="social__dot social__dot--b"></span>
    <span class="social__dot social__dot--c"></span>
  </div>
  <div class="contact">
    <div class="contact__row"><svg viewBox="0 0 12 12"><circle cx="6" cy="6" r="5.2" fill="none" stroke="#fff" stroke-width="1.2"/><rect x="3" y="4" width="6" height="4" fill="none" stroke="#fff" stroke-width="0.9"/></svg>info@tidewispcruise.com</div>
    <div class="contact__row"><svg viewBox="0 0 12 12"><circle cx="6" cy="6" r="5.2" fill="none" stroke="#fff" stroke-width="1.2"/><circle cx="6" cy="6" r="2.6" fill="none" stroke="#fff" stroke-width="0.9"/></svg>www.tidewispcruise.com</div>
  </div>
</section>

<!-- Back side -->
<section class="card card--back">
  <div class="brand">
    <div class="brand__name"><span class="brand__dot"></span>tidewisp cruise</div>
    <div class="brand__tag">DOLPHIN TOURS AND BOAT CRUISES</div>
  </div>

  <div class="photo" role="img" aria-label="Photo of a white deck boat with a canopy on clear turquoise water"></div>

  <div class="panel"></div>
  <svg class="wave" viewBox="0 0 340 90" preserveAspectRatio="none" aria-hidden="true">
    <path d="M0,38 C90,10 200,62 340,24 L340,42 C200,80 90,28 0,56 Z" fill="#ffffff"/>
    <path d="M0,52 C90,26 200,78 340,40 L340,62 C200,98 90,46 0,76 Z" fill="#1fa3e0"/>
    <path d="M0,74 C90,44 200,96 340,60 L340,90 L0,90 Z" fill="#f58220"/>
  </svg>

  <div class="boat-spec">
    <div class="boat-spec__line1">RENT 24' HARBORLINE DECK BOAT</div>
    <div class="boat-spec__line2">WITH A CAPTAIN AS GUIDE</div>
  </div>
  <div class="divider"></div>
  <p class="promise">PERSONAL YOUR DAY<br>ON THE WATER!</p>
  <div class="cta">BOOK YOUR ADVENTURE TODAY!</div>
  <div class="phone">
    <svg viewBox="0 0 24 24" aria-hidden="true"><path d="M6.5,3 L9.5,3 L11,8 L8.8,9.6 C9.8,12 11.8,14.2 14.4,15.2 L16,13 L21,14.5 L21,17.5 C21,19 19.8,20.5 18,20.3 C10.5,19.6 4.4,13.5 3.7,6 C3.5,4.2 5,3 6.5,3 Z" fill="#fff"/></svg>
    (555)-203-7714
  </div>

  <svg class="footer-shape" viewBox="0 0 340 80" preserveAspectRatio="none" aria-hidden="true">
    <path d="M0,30 C110,8 230,6 340,22 L340,80 L0,80 Z" fill="#ffffff"/>
    <path d="M0,40 C110,18 230,16 340,32 L340,80 L0,80 Z" fill="#1fa3e0"/>
  </svg>
  <div class="listing-badge" aria-hidden="true"></div>
  <div class="contact">
    <div class="contact__row"><svg viewBox="0 0 12 12"><circle cx="6" cy="6" r="5.2" fill="none" stroke="#fff" stroke-width="1.2"/><rect x="3" y="4" width="6" height="4" fill="none" stroke="#fff" stroke-width="0.9"/></svg>info@tidewispcruise.com</div>
    <div class="contact__row"><svg viewBox="0 0 12 12"><circle cx="6" cy="6" r="5.2" fill="none" stroke="#fff" stroke-width="1.2"/><circle cx="6" cy="6" r="2.6" fill="none" stroke="#fff" stroke-width="0.9"/></svg>www.tidewispcruise.com</div>
  </div>
</section>

</body>
</html>
```